Business Card Design Project

We need a business card design for a management consultancy focused on financial innovation and digital money, run by experts from the Financial Services, Telecoms and Money Transfer industries.
Our products include services such as Mobile Payments, Mobile Money, Digital Wallets, Online Payments, Branchless Banking and more. We work with regulatory information, business plans, financial modelling, strategic planning, new products functional specification, new technologies evaluation, etc.
See company logo attached.
We would like to see 2 versions: one in portuguese and one in english (regarding data information). You can see below information needed (whenever there is a difference between the two versions, the first one is in english and the second one in portuguese).

Name
Position
Phone/ Tel: ++55-11-xxxx-xxxx
Cell/ Cel: ++55-11-9 xxxx-xxxx
Dr. Tavares Lobato Av., 318 - Tower II - 16th floor / Avenida Dr. Tavares Lobato, 318 - Torre II - 16o. andar
São Paulo - SP
01327-118 - Brazil/ 01327-118 - Brasil

Target Market(s)

Audience: C-level executives from banks, credit card companies, acquirers, IT developers, retailers

Industry/Entity Type

Financial

Requirements
Must have
• Must use the logo and information above. Front must have white background. Back side should have only logo.
Nice to have
• Back should be in another colour but if it seems too exxagerated, maintain back in white also.
Should not have
• Do not add other illustrations to the business card.

```html
<!DOCTYPE html>
<html lang="pt-BR">
<head>
<meta charset="utf-8">
<title>M Halvorsen – Business Cards</title>
<link rel="stylesheet" href="https://fonts.googleapis.com/css2?family=Marcellus&family=Open+Sans:wght@300;400;700&display=swap">
<style>
  :root {
    --stage: #262626;
    --card-white: #ffffff;
    --navy-deep: #0c1640;
    --navy-mid: #17307a;
    --blue-bright: #2456b0;
    --brand-navy: #1b2a5c;
    --text-light: #dfe6f5;
    --text-white: #ffffff;
    --shadow: rgba(0, 0, 0, 0.45);
  }
  * { box-sizing: border-box; margin: 0; padding: 0; }
  html, body { width: 1200px; height: 1000px; overflow: hidden; }
  body {
    background: var(--stage);
    font-family: "Open Sans", Arial, sans-serif;
    position: relative;
  }
  .card-set {
    position: absolute;
    left: 120px;
    display: flex;
    gap: 80px;
  }
  .card-set--english { top: 150px; }
  .card-set--portuguese { top: 560px; }
  .card {
    width: 440px;
    height: 252px;
    border-radius: 3px;
    box-shadow: 0 14px 30px var(--shadow);
    position: relative;
    overflow: hidden;
  }
  .card--front {
    background: var(--card-white);
    display: flex;
    align-items: center;
    justify-content: center;
  }
  .brand {
    display: flex;
    flex-direction: column;
    align-items: flex-start;
    color: var(--brand-navy);
  }
  .brand__row {
    display: flex;
    align-items: center;
    gap: 12px;
  }
  .brand__mark {
    width: 30px;
    height: 30px;
    background: var(--brand-navy);
  }
  .brand__name {
    font-family: "Marcellus", Georgia, serif;
    font-size: 34px;
    letter-spacing: 1px;
    line-height: 1;
  }
  .brand__tagline {
    font-family: "Marcellus", Georgia, serif;
    font-size: 15px;
    letter-spacing: 1.2px;
    margin-top: 8px;
    margin-left: 42px;
    color: #222;
  }
  .card--back {
    background: linear-gradient(200deg, var(--blue-bright) 0%, var(--navy-mid) 45%, var(--navy-deep) 100%);
    color: var(--text-light);
    padding: 30px 34px;
    text-align: right;
  }
  .contact__name {
    font-weight: 700;
    font-size: 18px;
    color: var(--text-white);
  }
  .contact__position {
    font-weight: 300;
    font-size: 12px;
    margin-bottom: 14px;
  }
  .contact__lines {
    font-weight: 300;
    font-size: 11.5px;
    line-height: 1.55;
  }
  .contact__postcode { margin-top: 8px; }
</style>
</head>
<body>
  <section class="card-set card-set--english" aria-label="English version">
    <article class="card card--front">
      <div class="brand">
        <div class="brand__row">
          <span class="brand__mark"></span>
          <span class="brand__name">M HALVORSEN</span>
        </div>
        <span class="brand__tagline">MANAGEMENT CONSULTING</span>
      </div>
    </article>
    <article class="card card--back">
      <p class="contact__name">Name here</p>
      <p class="contact__position">Position</p>
      <div class="contact__lines">
        <p>Phone ++55-11-xxxx-xxxx</p>
        <p>Cell ++55-11-xxxx-xxxx</p>
        <p>Dr. Tavares Lobato Av.,</p>
        <p>318 - Tower II - 16th floor</p>
        <p>São Paulo</p>
        <p class="contact__postcode">01327-118 - Brazil</p>
      </div>
    </article>
  </section>

  <section class="card-set card-set--portuguese" aria-label="Versão em português">
    <article class="card card--front">
      <div class="brand">
        <div class="brand__row">
          <span class="brand__mark"></span>
          <span class="brand__name">M HALVORSEN</span>
        </div>
        <span class="brand__tagline">CONSULTORIA ESTRATÉGICA</span>
      </div>
    </article>
    <article class="card card--back">
      <p class="contact__name">Name here</p>
      <p class="contact__position">Position</p>
      <div class="contact__lines">
        <p>tel ++55-11-xxxx-xxxx</p>
        <p>Cel ++55-11-xxxx-xxxx</p>
        <p>Avenida Dr. Tavares Lobato,</p>
        <p>318 - Torre II - 16o. andar</p>
        <p>SP</p>
        <p class="contact__postcode">01327-118 - Brasil</p>
      </div>
    </article>
  </section>
</body>
</html>
```